Brightpath Systems Line Card

I need to create a one page line card that displays the services that my company provides and the certifications we hold.
Updates
I have an updated logo that I will post as soon as I get it later today. For now you can see an example at:
The new logo is very close to this and the colors are the same.
The file that I have posted is an example of what I think is a slick format. the upload is a two page document, but I really only like the first page. What I need a little bit of marketing and then room for the content that describes our core services and certifications.
The content of the line card needs to be divided into 9 categories:
Cloud (Virtual) Computing environments
Links are to our current brochures on these items for reference.
Greetings all,
Greetings everyone!
Target Market(s)
Small to Medium sized businesses as well as government institutions. This should be a one page "firm handshake" type exposure that tells the customer they are dealing with a first class professional operation.
Industry/Entity Type
It Company
Look and feel
Each slider illustrates characteristics of the customer's brand and the style your logo design should communicate.

```html
<!DOCTYPE html>
<html lang="en">
<head>
<meta charset="utf-8">
<title>Brightpath Systems Line Card</title>
<link href="https://fonts.googleapis.com/css2?family=Open+Sans:wght@400;600&display=swap" rel="stylesheet">
<style>
:root{
  --page:#ffffff;
  --trim:#9a9a9a;
  --ink:#4a4a4c;
  --headline:#4f4f51;
  --band-grey:#6b6c70;
  --band-orange:#ef7a34;
  --text-light:#ffffff;
  --ring:#f6b51c;
  --icon-blue:#1f7fc4;
  --icon-dark:#2a3a4a;
  --accent:#ef6b1f;
}
*{margin:0;padding:0;box-sizing:border-box}
html,body{width:864px;height:1200px;overflow:hidden;background:var(--page)}
body{font-family:"Open Sans",Arial,sans-serif;color:var(--ink)}
.card{position:relative;width:864px;height:1200px}
.trim-marks{position:absolute;inset:0}
.artwork{position:absolute;left:35px;top:38px;width:792px;height:620px}

.brand{position:absolute;left:540px;top:62px;display:flex;flex-direction:column}
.brand-row{display:flex;align-items:center;gap:12px}
.brand-mark{width:48px;height:48px;background:var(--accent)}
.brand-name{font-weight:600;font-size:20px;line-height:22px;color:var(--ink);letter-spacing:.5px;white-space:nowrap}
.brand-tagline{font-size:7px;letter-spacing:.8px;color:var(--ink);margin:3px 0 0 60px;white-space:nowrap}

.headline{position:absolute;left:0;top:0;width:864px;font-weight:400}
.headline span{position:absolute;white-space:nowrap;color:var(--headline)}
.hl-big-1{left:285px;top:148px;font-size:54px;line-height:60px}
.hl-small-1{right:88px;top:200px;font-size:31px;line-height:36px}
.hl-big-2{left:348px;top:224px;font-size:54px;line-height:60px}
.hl-small-2{left:612px;top:242px;font-size:31px;line-height:36px}

.services{position:absolute;left:84px;top:310px;width:694px;list-style:none}
.service{position:relative;height:89px;padding:7px 48px 0 39px;color:var(--text-light);box-shadow:0 6px 8px rgba(0,0,0,.25)}
.service.grey{background:var(--band-grey)}
.service.orange{background:var(--band-orange);padding-right:40px}
.service h2{font-weight:400;font-size:22px;line-height:30px}
.service p{font-size:15px;line-height:19.5px;margin-top:4px}
.service-icon{position:absolute;top:14px;width:60px;height:60px}
.grey .service-icon{left:-28px}
.orange .service-icon{right:-30px}
</style>
</head>
<body>
<div class="card">
  <svg class="trim-marks" width="864" height="1200" aria-hidden="true">
    <g stroke="var(--trim)" stroke-width="1">
      <line x1="0" y1="38" x2="22" y2="38"/><line x1="35" y1="0" x2="35" y2="24"/>
      <line x1="842" y1="38" x2="864" y2="38"/><line x1="827" y1="0" x2="827" y2="24"/>
      <line x1="0" y1="1160" x2="22" y2="1160"/><line x1="35" y1="1176" x2="35" y2="1200"/>
      <line x1="842" y1="1160" x2="864" y2="1160"/><line x1="827" y1="1176" x2="827" y2="1200"/>
    </g>
  </svg>

  <svg class="artwork" viewBox="0 0 792 620" role="img" aria-label="Flowing red, orange and gold light swooshes sweeping across the top left of the page">
    <defs>
      <linearGradient id="sweep" x1="0" y1="0" x2="1" y2="0.5">
        <stop offset="0" stop-color="#c8161d"/>
        <stop offset="0.3" stop-color="#e8411f"/>
        <stop offset="0.6" stop-color="#f7a23a" stop-opacity=".7"/>
        <stop offset="1" stop-color="#fff3d6" stop-opacity="0"/>
      </linearGradient>
      <linearGradient id="edge" x1="0" y1="0" x2="0" y2="1">
        <stop offset="0" stop-color="#d8261e"/>
        <stop offset="1" stop-color="#d8261e" stop-opacity="0"/>
      </linearGradient>
    </defs>
    <rect x="0" y="0" width="792" height="300" fill="url(#sweep)"/>
    <rect x="0" y="0" width="50" height="620" fill="url(#edge)"/>
  </svg>

  <div class="brand">
    <div class="brand-row">
      <div class="brand-mark"></div>
      <div class="brand-name">BRIGHTPATH SYSTEMS</div>
    </div>
    <div class="brand-tagline">MANAGED IT FOR GROWING TEAMS</div>
  </div>

  <h1 class="headline">
    <span class="hl-big-1">Your success</span>
    <span class="hl-small-1">is our success and as</span>
    <span class="hl-big-2">You grow</span>
    <span class="hl-small-2">we grow</span>
  </h1>

  <ul class="services">
    <li class="service grey">
      <svg class="service-icon" viewBox="0 0 60 60" aria-hidden="true"><circle cx="30" cy="30" r="28" fill="#fff" stroke="var(--ring)" stroke-width="4"/><circle cx="30" cy="30" r="16" fill="var(--icon-blue)"/><path d="M14 30h32M30 14v32M20 20q10 10 20 0M20 40q10-10 20 0" stroke="#fff" stroke-width="1.5" fill="none"/></svg>
      <h2>Outsourced IT</h2>
      <p>Brightpath Systems provides customized Proactive IT monitoring and support that. Reduce downtime, increase profitability, and make your technology work for you</p>
    </li>
    <li class="service orange">
      <svg class="service-icon" viewBox="0 0 60 60" aria-hidden="true"><circle cx="30" cy="30" r="28" fill="#fff" stroke="var(--ring)" stroke-width="4"/><path d="M18 28a12 12 0 0 1 20-8l-4 4h10V14l-3 3A16 16 0 0 0 14 28z" fill="var(--icon-blue)"/><path d="M42 32a12 12 0 0 1-20 8l4-4H16v10l3-3a16 16 0 0 0 27-11z" fill="var(--icon-dark)"/></svg>
      <h2>Backup and Disaster Recovery</h2>
      <p>Bulletproof your Data Protection with the Highest Industry Standards in an All In One Backup &amp; Business Continuity Solution</p>
    </li>
    <li class="service grey">
      <svg class="service-icon" viewBox="0 0 60 60" aria-hidden="true"><circle cx="30" cy="30" r="28" fill="#fff" stroke="var(--ring)" stroke-width="4"/><g stroke="var(--icon-blue)" stroke-width="3" fill="none" stroke-linecap="round"><path d="M18 28a17 17 0 0 1 24 0"/><path d="M22 33a11 11 0 0 1 16 0"/></g><circle cx="30" cy="39" r="3" fill="var(--icon-blue)"/></svg>
      <h2>Cloud (Virtual) Computing environments</h2>
      <p>Eliminate expensive start up costs and IT management overhead with enterprise level cloud solutions</p>
    </li>
    <li class="service orange">
      <svg class="service-icon" viewBox="0 0 60 60" aria-hidden="true"><circle cx="30" cy="30" r="28" fill="#fff" stroke="var(--ring)" stroke-width="4"/><rect x="18" y="18" width="20" height="26" fill="#fff" stroke="var(--icon-dark)" stroke-width="2"/><path d="M22 26h12M22 31h12M22 36h8" stroke="var(--icon-blue)" stroke-width="2"/><path d="M34 36l10-16 3 2-10 16z" fill="var(--icon-dark)"/></svg>
      <h2>Office Cloud Suite</h2>
      <p>The reliability of Quillworks Office has now been enhanced with cloud features</p>
    </li>
    <li class="service grey">
      <svg class="service-icon" viewBox="0 0 60 60" aria-hidden="true"><circle cx="30" cy="30" r="28" fill="#fff" stroke="var(--ring)" stroke-width="4"/><path d="M22 22v16h14M22 30h14" stroke="#555" stroke-width="2" fill="none"/><rect x="15" y="16" width="13" height="9" fill="var(--accent)"/><rect x="33" y="26" width="13" height="9" fill="var(--accent)"/><rect x="33" y="35" width="13" height="9" fill="var(--accent)"/></svg>
      <h2>Network Security</h2>
      <p>How secure is your network? Are you at risk? It’s time to get proactive! Protect your Business Inside and Out</p>
    </li>
    <li class="service orange">
      <svg class="service-icon" viewBox="0 0 60 60" aria-hidden="true"><circle cx="30" cy="30" r="28" fill="#fff" stroke="var(--ring)" stroke-width="4"/><rect x="21" y="15" width="18" height="30" rx="3" fill="#c9ced4" stroke="#555"/><rect x="24" y="19" width="12" height="18" fill="var(--icon-blue)"/></svg>
      <h2>Server Care</h2>
      <p>Flat Rate Managed Server Care is a complete, 24x7x365 server monitoring, remediation, maintenance and management solution</p>
    </li>
    <li class="service grey">
      <svg class="service-icon" viewBox="0 0 60 60" aria-hidden="true"><circle cx="30" cy="30" r="28" fill="#fff" stroke="var(--ring)" stroke-width="4"/><rect x="15" y="19" width="30" height="20" rx="2" fill="#555"/><rect x="18" y="22" width="24" height="14" fill="var(--icon-blue)"/><rect x="24" y="40" width="12" height="3" fill="#555"/></svg>
      <h2>Desktop and User Care</h2>
      <p>Proactive Maintenance and Security Updates for your Workstations, Remote and On Site IT Support for your Staff</p>
    </li>
    <li class="service orange">
      <svg class="service-icon" viewBox="0 0 60 60" aria-hidden="true"><circle cx="30" cy="30" r="28" fill="#fff" stroke="var(--ring)" stroke-width="4"/><rect x="15" y="20" width="30" height="22" rx="3" fill="#d8dde2" stroke="#555"/><rect x="18" y="17" width="9" height="24" rx="3" fill="#8d949b"/><g fill="#555"><rect x="30" y="24" width="3" height="3"/><rect x="35" y="24" width="3" height="3"/><rect x="40" y="24" width="3" height="3"/><rect x="30" y="30" width="3" height="3"/><rect x="35" y="30" width="3" height="3"/><rect x="40" y="30" width="3" height="3"/><rect x="30" y="36" width="3" height="3"/><rect x="35" y="36" width="3" height="3"/><rect x="40" y="36" width="3" height="3"/></g></svg>
      <h2>VOIP</h2>
      <p>Businesses that utilize VoIP save money and gain more communication features. Make a Smart Investment with your Small Business by switching to VoIP</p>
    </li>
    <li class="service grey">
      <svg class="service-icon" viewBox="0 0 60 60" aria-hidden="true"><circle cx="30" cy="30" r="28" fill="#fff" stroke="var(--ring)" stroke-width="4"/><circle cx="24" cy="24" r="6" fill="var(--icon-dark)"/><path d="M13 42a11 11 0 0 1 22 0z" fill="var(--icon-dark)"/><circle cx="36" cy="27" r="6" fill="var(--icon-blue)"/><path d="M25 45a11 11 0 0 1 22 0z" fill="var(--icon-blue)"/></svg>
      <h2>Vendor Management</h2>
      <p>Get better, faster support for your third party hardware and software investments and one point of contact for all of your vendor relationships</p>
    </li>
  </ul>
</div>
</body>
</html>
```